International Digitally Led Media Agency Requires a New Website

Brief Outline

• We are a growing business that has been established for approximately 2 years.

• Our current website did the job when Corvend Media began but it has not developed and progressed alongside the business (currently it does not represent nor portray the business appropriately).

• Corvend Media is a digitally led media agency that has numerous arms; 1) production based work (e.g. Paid Advertising, etc.) 2) consultancy and 3) Offline media (such as outdoor, TV, Radio)

• The business is globally focused and the website must reflect this.

• The new website is to portray the business more professionally with thought leadership at the forefront.

• The tone and voice of the website is to be clear, concise and straight talking.

• The website isn't to be a driver of new business (e.g. conversion based for enquiries) but is to support external new business activities. However, the website is to support the thought leadership marketing (specifically around content marketing - webinars, whitepapers, social, etc).

• We must be able to edit/upload/add content to the website very easily.

The current website is www.corvend-media.example

Current clients include
J&T - www.j&t.example
Folmary Trudesse - www.ft.example
KX Glow - www.kxglow.example
Lungwise UK - www.lungwise.example.uk
The Vantry Academy - www.vantry-academy.example.uk
Hale Retirement - www.haleretirement.example
Quillet Credit - www.quilletcredit.example.uk
DLMorvat - www.dl-morvat.example.uk
Perravine Lodging Collective - www.plc-lodging.example
Brindlewick - www.brindlewick.example
Varnique - www.varniqueit.example

Reason: We gave some delayed feedback to some desginers looking to enter the project and want to give them a chance to submit their designs.

Target Market(s)

Key decision makers within brands. Marketing Executives/Managers/Directors, Procurement Executives/Managers/Directors, Company Owners, CEO's /MD's

Industry/Entity Type

Business

Coding

Coded - Design and coding required

Number of Pages Required

5+ page

Font styles to use
Sans Serif

Requirements
Must have
• We definitely want video capability and the ability to add pages ourselves.
• We would like the layout to look something like
• HOME
•   
• 7dash3 > CASE STUDIES
• WHAT WE DO > CASE STUDIES
•  
• CONTACT
•  
• CLIENT LOGIN
Nice to have
• Social feeds

```html
<!DOCTYPE html>
<html lang="en">
<head>
<meta charset="utf-8">
<title>Corvend Media</title>
<link href="https://fonts.googleapis.com/css2?family=Open+Sans:wght@300;400;600&family=Roboto+Condensed:wght@400;700&family=Roboto:wght@300;400;500&display=swap" rel="stylesheet">
<style>
:root{
  --red:#9b1a33;
  --red-bright:#c0223f;
  --ink:#2b2b2b;
  --muted:#777;
  --light:#efefef;
  --footer:#1e1e1e;
  --white:#fff;
  --head:"Roboto Condensed",sans-serif;
  --body:"Open Sans",sans-serif;
  --nav:"Roboto",sans-serif;
}
*{box-sizing:border-box;margin:0;padding:0}
html,body{width:1200px;height:3237px;overflow:hidden}
body{font-family:var(--body);color:var(--ink);background:var(--white);position:relative}
section,header,footer{position:absolute;left:0;width:1200px}

/* nav */
.site-nav{top:0;height:65px;background:var(--red);z-index:3;display:flex;padding-left:198px}
.site-nav a{font-family:var(--nav);font-size:17px;color:var(--white);text-decoration:none;height:65px;line-height:65px;padding:0 19px;text-transform:uppercase}
.site-nav a.active{background:#2a2a2a;padding:0 35px}

/* hero */
.hero{top:0;height:676px;overflow:hidden;background:#1d1f25}
.hero-photo{position:absolute;inset:0;background:
  radial-gradient(ellipse 420px 300px at 320px 330px,rgba(150,140,135,.45),transparent 70%),
  radial-gradient(ellipse 700px 180px at 800px 430px,rgba(190,120,60,.35),transparent 70%),
  radial-gradient(ellipse 500px 140px at 300px 470px,rgba(170,100,55,.28),transparent 70%),
  linear-gradient(180deg,#2a2f3a 0%,#3b3f4a 30%,#4b4440 55%,#3a302c 75%,#1c1a1a 100%)}
.hero-shade{position:absolute;inset:0;background:rgba(20,20,24,.25)}
.brand{position:absolute;left:440px;top:228px}
.brand-row{display:flex;align-items:center;gap:20px}
.brand-dot{width:24px;height:24px;border-radius:50%;background:var(--red)}
.brand-name{font-family:var(--nav);font-size:44px;letter-spacing:8px;color:#d6d6d6;font-weight:400}
.brand-tag{font-family:var(--nav);font-size:22px;letter-spacing:7px;color:#bdbdbd;margin:10px 0 0 44px;font-weight:300}
.hero-title{position:absolute;left:0;width:1200px;top:452px;text-align:center;font-family:var(--body);font-size:36px;line-height:50px;color:#cfcfcf;font-weight:300}

/* welcome */
.welcome{top:676px;height:446px;background:var(--light)}
.welcome h2{position:absolute;left:80px;top:56px;font-family:var(--head);font-size:42px;font-weight:400;color:#3a3a3a}
h2 em{font-style:normal;color:var(--red)}
.welcome .copy{position:absolute;left:80px;top:114px;width:515px;font-size:13px;line-height:26px;color:#666}
.welcome .copy p+p{margin-top:4px}
.btn-solid{position:absolute;left:80px;top:323px;width:194px;height:65px;background:var(--red);color:var(--white);font-family:var(--nav);font-size:19px;text-transform:uppercase;display:flex;align-items:center;justify-content:center}
.accent-rule{position:absolute;left:617px;top:69px;width:4px;height:172px;background:var(--red)}
.video{position:absolute;left:632px;top:64px;width:460px;height:322px;background:
  radial-gradient(ellipse 260px 60px at 300px 250px,rgba(220,150,90,.45),transparent 70%),
  radial-gradient(ellipse 160px 220px at 90px 150px,rgba(170,180,200,.35),transparent 70%),
  linear-gradient(180deg,#4a5a7a 0%,#5d6687 30%,#3c3f5a 60%,#2a2634 82%,#151419 100%)}
.video svg{position:absolute;left:190px;top:121px}

/* services */
.services{top:1122px;height:553px;background:var(--white);text-align:center}
.services h2{position:absolute;left:0;width:1200px;top:62px;font-family:var(--head);font-size:42px;font-weight:400;color:#3a3a3a}
.services .lead{position:absolute;left:134px;width:932px;top:128px;font-size:13px;line-height:29px;color:#777}
.service{position:absolute;top:190px;width:340px}
.service svg{display:block;margin:0 auto}
.service h3{font-family:var(--nav);font-weight:500;font-size:18px;margin-top:18px;text-transform:uppercase;color:#222}
.service p{font-size:13px;line-height:29px;color:#777;margin-top:8px}
.service .chev{margin-top:6px}

/* band */
.cta-band{top:1675px;height:155px;background:var(--red);color:var(--white)}
.cta-band h2{position:absolute;left:80px;top:32px;font-family:var(--head);font-size:31px;font-weight:400}
.cta-band p{position:absolute;left:80px;top:80px;width:800px;font-size:13px;line-height:28px}
.btn-ghost{position:absolute;left:956px;top:54px;width:166px;height:56px;border:2px solid var(--white);font-family:var(--nav);font-size:17px;text-transform:uppercase;display:flex;align-items:center;justify-content:center}

/* case study */
.case{top:1830px;height:371px;overflow:hidden;background:
  radial-gradient(ellipse 500px 120px at 300px 320px,rgba(170,110,60,.35),transparent 70%),
  radial-gradient(ellipse 600px 140px at 900px 300px,rgba(160,100,60,.3),transparent 70%),
  radial-gradient(ellipse 600px 160px at 600px 60px,rgba(110,110,125,.35),transparent 70%),
  linear-gradient(180deg,#24262d,#33312f 55%,#1f1c1b)}
.case h2{position:absolute;left:0;width:1200px;top:50px;text-align:center;font-family:var(--head);font-size:38px;font-weight:400;color:#9c9c9c}
.case-thumb{position:absolute;left:97px;top:127px;width:212px;height:147px;border:4px solid #eee;background:
  radial-gradient(ellipse 60px 40px at 110px 100px,rgba(190,40,60,.55),transparent 70%),
  linear-gradient(160deg,#8a7464 0%,#d8d0c4 45%,#b9aa98 65%,#6d5b4d 100%)}
.case h3{position:absolute;left:330px;top:128px;font-family:var(--head);font-size:15px;font-weight:400;color:var(--white);text-transform:uppercase}
.case .copy{position:absolute;left:330px;top:160px;width:740px;font-size:13px;line-height:25px;color:#aaa}
.case .more{position:absolute;left:330px;top:246px;font-size:13px;color:var(--red-bright)}
.dots{position:absolute;left:568px;top:297px;display:flex;gap:6px}
.dots i{width:9px;height:9px;border-radius:50%;background:#888}
.dots i.on{background:var(--red)}

/* blog */
.blog{top:2201px;height:557px;background:var(--white)}
.blog h2{position:absolute;left:0;width:1200px;top:56px;text-align:center;font-family:var(--head);font-size:40px;font-weight:400;color:#3a3a3a}
.post{position:absolute;top:127px;width:332px}
.post-img{height:197px}
.post h3{font-family:var(--head);font-size:19px;font-weight:400;color:#222;margin-top:24px}
.post time{display:flex;align-items:center;gap:10px;color:var(--red);font-size:14px;margin-top:12px}
.post p{font-size:12.5px;line-height:25px;color:#777;margin-top:8px}

/* clients */
.clients{top:2758px;height:166px;background:#ececec}
.arrow{position:absolute;top:56px;width:42px;height:42px;border:1px solid #888;border-radius:50%}
.arrow svg{position:absolute;left:13px;top:12px}
.client{position:absolute;top:38px;height:90px;width:180px;display:flex;align-items:center;justify-content:center;text-align:center;font-family:var(--head);font-weight:700;font-size:19px;line-height:23px;color:#444}

/* footer */
.site-footer{top:2924px;height:248px;background:var(--footer);color:#bbb}
.fcol{position:absolute;top:37px}
.fcol h4{font-family:var(--nav);font-weight:500;font-size:16px;color:var(--red);text-transform:uppercase;letter-spacing:.5px}
.links{list-style:none;margin-top:16px}
.links li{font-size:13px;line-height:27px;display:flex;align-items:center;gap:12px}
.links li::before{content:"";width:7px;height:7px;background:var(--red)}
.contact-line{display:flex;gap:14px;font-size:13px;line-height:22px;margin-top:12px}
.contact-line svg{flex:none;margin-top:3px}
.fpost{display:flex;gap:12px;margin-top:14px;width:240px}
.avatar{flex:none;width:50px;height:50px;border-radius:50%;background:linear-gradient(135deg,#9a8a7c,#6a5e56)}
.fpost p{font-size:12.5px;line-height:18px}
.fpost time{display:block;font-size:11px;color:var(--red)}
.social{display:flex;align-items:center;gap:14px;margin-top:14px;font-size:14px}
.social i{width:36px;height:36px;border-radius:50%;background:var(--red)}
.legal{position:absolute;left:0;width:1200px;top:3172px;height:65px;background:var(--red);color:#f0d8dd;text-align:center;line-height:65px;font-size:14px}
.legal b{font-weight:400;color:#1a1a1a}
</style>
</head>
<body>

<header class="site-nav">
  <a class="active">Home</a><a>Our Work</a><a>Who We Are</a><a>Client Login</a><a>Blog</a><a>Contact</a>
</header>

<section class="hero">
  <div class="hero-photo" role="img" aria-label="Hand holding a smartphone in front of a city skyline at dusk"></div>
  <div class="hero-shade"></div>
  <div class="brand">
    <div class="brand-row"><span class="brand-dot"></span><span class="brand-name">CORVEND MEDIA</span></div>
    <div class="brand-tag">WE MAKE AMAZING</div>
  </div>
  <h1 class="hero-title">Got the feeling your digital marketing just isn't<br>quite 'there'?</h1>
</section>

<section class="welcome">
  <h2>Welcome To <em>Corvend Media</em></h2>
  <div class="copy">
    <p>There are too many large agency networks. Consolidation is everywhere, giving clients less choice and choking media creativity for the benefit of perceived economies of scale.</p>
    <p>There are too few agencies being transparent. Do you really know how your agency makes its revenue? Are their decisions based on what is best for your brand or are there other incentives involved? Too many of these agencies put quality of work second to income.</p>
  </div>
  <div class="btn-solid">Know More</div>
  <span class="accent-rule"></span>
  <div class="video" role="img" aria-label="Video still of a modern city skyline with a curved bridge at night">
    <svg width="80" height="80" viewBox="0 0 80 80"><circle cx="40" cy="40" r="36" fill="none" stroke="#9b1a33" stroke-width="4"/><path d="M31 22 L58 40 L31 58 Z" fill="#9b1a33"/></svg>
  </div>
</section>

<section class="services">
  <h2>What <em>We Do ?</em></h2>
  <p class="lead">There are too many large agency networks. Consolidation is everywhere, giving clients less choice and choking media creativity for the benefit of perceived economies of scale. There are too few agencies being transparent.</p>

  <div class="service" style="left:67px">
    <svg width="140" height="140" viewBox="0 0 140 140"><path d="M95 10 A62 62 0 1 0 112 118" fill="none" stroke="#9b1a33" stroke-width="3"/><g fill="none" stroke="#444" stroke-width="5"><circle cx="55" cy="52" r="12"/><circle cx="82" cy="52" r="12"/><rect x="38" y="66" width="52" height="32" rx="4"/><path d="M90 76 L104 68 L104 96 L90 88"/></g></svg>
    <h3>Production Based Work</h3>
    <p>We make your brand famous. To do this we optimise your website or any digital assets you have, so they can be found online.</p>
    <svg class="chev" width="16" height="14" viewBox="0 0 16 14"><path d="M2 2 L8 7 L14 2 M2 7 L8 12 L14 7" fill="none" stroke="#9b1a33" stroke-width="2"/></svg>
  </div>

  <div class="service" style="left:430px">
    <svg width="140" height="140" viewBox="0 0 140 140"><path d="M95 10 A62 62 0 1 0 112 118" fill="none" stroke="#9b1a33" stroke-width="3"/><g fill="#444"><circle cx="52" cy="48" r="8"/><circle cx="88" cy="48" r="8"/><rect x="44" y="60" width="16" height="22" rx="3"/><rect x="80" y="60" width="16" height="22" rx="3"/><rect x="40" y="84" width="60" height="6"/><rect x="52" y="90" width="6" height="16"/><rect x="82" y="90" width="6" height="16"/></g></svg>
    <h3>Consultancy</h3>
    <p>We make your brand famous. To do this we optimise your website or any digital assets you have, so they can be found online.</p>
    <svg class="chev" width="16" height="14" viewBox="0 0 16 14"><path d="M2 2 L8 7 L14 2 M2 7 L8 12 L14 7" fill="none" stroke="#9b1a33" stroke-width="2"/></svg>
  </div>

  <div class="service" style="left:786px">
    <svg width="140" height="140" viewBox="0 0 140 140"><path d="M95 10 A62 62 0 1 0 112 118" fill="none" stroke="#9b1a33" stroke-width="3"/><g fill="#444"><rect x="30" y="60" width="12" height="20"/><path d="M42 60 L82 42 L82 98 L42 80 Z"/></g><g fill="none" stroke="#444" stroke-width="4"><path d="M92 58 Q98 70 92 82"/><path d="M100 50 Q110 70 100 90"/></g></svg>
    <h3>Offline Media</h3>
    <p>We make your brand famous. To do this we optimise your website or any digital assets you have, so they can be found online.</p>
    <svg class="chev" width="16" height="14" viewBox="0 0 16 14"><path d="M2 2 L8 7 L14 2 M2 7 L8 12 L14 7" fill="none" stroke="#9b1a33" stroke-width="2"/></svg>
  </div>
</section>

<section class="cta-band">
  <h2>Corvend Media</h2>
  <p>There are too many large agency networks. Consolidation is everywhere, giving clients less choice and choking media creativity for the benefit of perceived economies of scale. There are too few agencies being transparent.</p>
  <div class="btn-ghost">Client Login</div>
</section>

<section class="case" role="region" aria-label="Case study over a dimmed city skyline at night">
  <h2>Case <em>Study</em></h2>
  <div class="case-thumb" role="img" aria-label="Campaign photo of a person working at a desk with posters"></div>
  <h3>Push Past Plain. Surpass Expectations</h3>
  <p class="copy">Kestra Sport exists to multiply human performance. Corvend exists to deliver amazing work for amazing brands. Our role was to amplify their Push Past Plain campaign in the US. To inspire athletes of all levels to do that extra rep or run that extra mile. We had two days.</p>
  <span class="more">Read More...»</span>
  <div class="dots"><i></i><i></i><i class="on"></i><i></i></div>
</section>

<section class="blog">
  <h2>Latest <em>Blog</em></h2>
  <article class="post" style="left:78px">
    <div class="post-img" role="img" aria-label="Person working at a desk in a studio with posters on a brick wall" style="background:radial-gradient(ellipse 80px 50px at 180px 130px,rgba(190,40,60,.55),transparent 70%),linear-gradient(120deg,#4a3628 0%,#8c6e58 30%,#d9d2c6 55%,#a58a70 75%,#3d2c22 100%)"></div>
    <h3>Dana Whitlow report and it is all mobile</h3>
    <time><svg width="14" height="14" viewBox="0 0 14 14"><rect x="1" y="2" width="12" height="11" fill="none" stroke="#9b1a33" stroke-width="1.6"/><rect x="1" y="2" width="12" height="3" fill="#9b1a33"/></svg>Jun 07, 2016</time>
    <p>It's out! The 2016 Dana Whitlow report came out this week and it is all mobile, mobile, mobile! There are three key trends.</p>
  </article>
  <article class="post" style="left:434px">
    <div class="post-img" role="img" aria-label="Open-plan office with people at computer desks" style="background:radial-gradient(ellipse 140px 50px at 170px 150px,rgba(60,80,110,.45),transparent 70%),linear-gradient(180deg,#e8e8e4 0%,#c9ccd0 40%,#8d949c 70%,#5b626c 100%)"></div>
    <h3>Copy writing and paid search</h3>
    <time><svg width="14" height="14" viewBox="0 0 14 14"><rect x="1" y="2" width="12" height="11" fill="none" stroke="#9b1a33" stroke-width="1.6"/><rect x="1" y="2" width="12" height="3" fill="#9b1a33"/></svg>May 25, 2016</time>
    <p>Will the skills of copy writing finally be valued in paid search ads? Searchly yesterday released the news that there is going to be a change.</p>
  </article>
  <article class="post" style="left:790px">
    <div class="post-img" role="img" aria-label="Hands typing on a laptop keyboard" style="background:radial-gradient(ellipse 110px 70px at 240px 90px,rgba(220,160,140,.8),transparent 70%),linear-gradient(135deg,#1f1f22 0%,#4a4a4e 40%,#b9b5b2 75%,#e6e2de 100%)"></div>
    <h3>Viewability...what a missed opportunity</h3>
    <time><svg width="14" height="14" viewBox="0 0 14 14"><rect x="1" y="2" width="12" height="11" fill="none" stroke="#9b1a33" stroke-width="1.6"/><rect x="1" y="2" width="12" height="3" fill="#9b1a33"/></svg>Apr 15, 2016</time>
    <p>There was a lot of furore in the market 12-18 months ago about the lack of viewability with digital and the money wasted on ads that no one saw.</p>
  </article>
</section>

<section class="clients">
  <span class="arrow" style="left:76px"><svg width="14" height="18" viewBox="0 0 14 18"><path d="M10 2 L3 9 L10 16" fill="none" stroke="#666" stroke-width="2"/></svg></span>
  <div class="client" style="left:124px">Lungwise UK</div>
  <div class="client" style="left:298px">Hale Retirement</div>
  <div class="client" style="left:490px">Perravine Lodging Collective</div>
  <div class="client" style="left:667px">Brindlewick</div>
  <div class="client" style="left:892px">Folmary Trudesse</div>
  <span class="arrow" style="left:1080px"><svg width="14" height="18" viewBox="0 0 14 18"><path d="M4 2 L11 9 L4 16" fill="none" stroke="#666" stroke-width="2"/></svg></span>
</section>

<footer class="site-footer">
  <div class="fcol" style="left:80px">
    <h4>Usefull Links</h4>
    <ul class="links"><li>Home</li><li>Our Work</li><li>Who We Are</li><li>Client Login</li><li>Blog</li><li>Contact</li></ul>
  </div>
  <div class="fcol" style="left:334px">
    <h4>Get In Touch</h4>
    <div class="contact-line"><svg width="14" height="18" viewBox="0 0 14 18"><path d="M7 1 A6 6 0 0 1 13 7 C13 11 7 17 7 17 C7 17 1 11 1 7 A6 6 0 0 1 7 1 Z" fill="#9b1a33"/><circle cx="7" cy="7" r="2.2" fill="#1e1e1e"/></svg><span style="color:#ddd">Corvend Media<br><br>48 Fennick Row London,<br>EC9 4ZZ</span></div>
    <div class="contact-line"><svg width="14" height="18" viewBox="0 0 14 18"><rect x="2" y="1" width="10" height="16" rx="2" fill="#9b1a33"/></svg><span>+44 20 7946 0123</span></div>
    <div class="contact-line"><svg width="16" height="12" viewBox="0 0 16 12"><rect width="16" height="12" fill="#9b1a33"/><path d="M0 0 L8 7 L16 0" fill="none" stroke="#1e1e1e" stroke-width="1.5"/></svg><span>contact@corvend-media.example</span></div>
  </div>
  <div class="fcol" style="left:611px">
    <h4>Latest Blog</h4>
    <div class="fpost"><span class="avatar" role="img" aria-label="Author avatar"></span><p>Dana Whitlow report and it is all mobile, mobile !<time>Jun 07, 2016</time></p></div>
    <div class="fpost"><span class="avatar" role="img" aria-label="Author avatar"></span><p>Viewability...what a missed opportunity<time>Apr 15, 2016</time></p></div>
  </div>
  <div class="fcol" style="left:883px">
    <h4>Follow Us</h4>
    <div class="social"><i></i>Clipreel</div>
    <div class="social"><i></i>Chirpline</div>
    <div class="social"><i></i>Streamtube</div>
  </div>
</footer>

<div class="legal">© <b>Corvend Media</b> - 2016, All rights reserved.</div>

</body>
</html>
```